Pamphlet that will be placed inside hotel rooms for laundry service

We are offering all guests of a Hotel property in NYC next day laundry services.

Things to include on the flyer-
COMPLEMENTARY pick up and delivery
COMPLEMENTARY Brisa and Velvo!
NEXT DAY SERVICE
Smells great
We keep Colors Brighter!
Next day delivery
1.10/Lb.
Email notifications
Please use our logo and the logo of hotel (attached)

All they have to do is place an order at www.quikwashly.example and leave it by the front desk at the hotel,

All laundry will be delivered next day professionally folded

Target Market(s)

this will be going inside very fancy hotels
we are looking for a clean look nothing to busy

Industry/Entity Type

Hotel

Font styles to use
Other font styles liked:
• Harababa

Requirements
Must have
• The font and color codes for the logo are as follows:
• Logo font: Harabara
• Slogan font: Swiss 721 Light Extended BT
• Dark blue: C 100 M 88 Y 0 K 0
• Light blue: C 85 M 50 Y 0 K 0
• Orange: C 0 M 80 Y 95 K 0
• Violet: C 85 M 100 Y 0 K 0

```html
<!DOCTYPE html>
<html lang="en">
<head>
<meta charset="utf-8">
<title>Next Day Laundry Services</title>
<link rel="stylesheet" href="https://fonts.googleapis.com/css2?family=Montserrat:ital,wght@0,500;0,700;0,800;0,900;1,500;1,700&display=swap">
<style>
  :root {
    --navy: #1f2a6e;
    --light-blue: #3d7fc6;
    --orange: #f15a22;
    --violet: #3b1e8c;
    --ray: #dbe6f3;
    --white: #ffffff;
    --paper: #f6f9fc;
  }
  html, body {
    margin: 0;
    padding: 0;
    overflow: hidden;
    background: var(--white);
  }
  .flyer {
    position: relative;
    width: 847px;
    height: 1200px;
    overflow: hidden;
    font-family: "Montserrat", sans-serif;
    color: var(--navy);
    background: radial-gradient(circle at 50% 45%, var(--paper) 0%, var(--ray) 70%, #cddcee 100%);
  }
  .header {
    position: absolute;
    left: 42px;
    top: 28px;
    width: 778px;
    height: 140px;
    box-sizing: border-box;
    background: var(--white);
    border-radius: 26px;
    box-shadow: 0 2px 6px rgba(31, 42, 110, 0.18);
    display: flex;
    align-items: center;
  }
  .hotel-mark {
    width: 170px;
    display: flex;
    flex-direction: column;
    align-items: center;
    gap: 8px;
    margin-left: 18px;
  }
  .hotel-mark__square {
    width: 48px;
    height: 48px;
    background: var(--violet);
  }
  .hotel-mark__name {
    font-weight: 700;
    font-size: 15px;
    letter-spacing: 0.5px;
    white-space: nowrap;
    color: var(--navy);
    text-transform: uppercase;
  }
  .header__title {
    margin: 0 0 0 40px;
    font-weight: 900;
    font-size: 42px;
    line-height: 1.12;
    letter-spacing: 1.5px;
    color: var(--navy);
    text-transform: uppercase;
  }
  .laundry-photo {
    position: absolute;
    left: 160px;
    top: 180px;
    width: 530px;
    height: 395px;
    border-radius: 40% 40% 12% 12%;
    background:
      radial-gradient(ellipse at 50% 28%, #f5a623 0%, #f07a1e 30%, #d9361e 55%, transparent 70%),
      linear-gradient(180deg, transparent 45%, #eef2f6 55%, #d5dde6 100%);
  }
  .services-band {
    position: absolute;
    left: 0;
    top: 608px;
    width: 847px;
    height: 46px;
    background: var(--navy);
  }
  .services-title {
    position: absolute;
    left: 110px;
    top: 588px;
    width: 627px;
    height: 88px;
    margin: 0;
    background: var(--white);
    color: var(--orange);
    font-weight: 800;
    font-size: 46px;
    line-height: 88px;
    white-space: nowrap;
    text-align: center;
    text-transform: uppercase;
  }
  .services-list {
    position: absolute;
    left: 0;
    top: 712px;
    width: 847px;
    margin: 0;
    padding: 0;
    list-style: none;
    text-align: center;
  }
  .services-list__item {
    display: flex;
    justify-content: center;
    align-items: center;
    gap: 18px;
    height: 49px;
    font-style: italic;
    font-weight: 700;
    font-size: 29px;
    white-space: nowrap;
    color: var(--navy);
  }
  .tick {
    width: 26px;
    height: 26px;
    flex: none;
  }
  .order-bar {
    position: absolute;
    left: 28px;
    top: 1042px;
    width: 792px;
    height: 132px;
    border-radius: 30px;
    background: var(--navy);
    display: flex;
    align-items: center;
  }
  .brand {
    width: 200px;
    flex: none;
    display: flex;
    flex-direction: column;
    align-items: center;
    gap: 6px;
    margin-left: 14px;
  }
  .brand__circle {
    width: 56px;
    height: 56px;
    border-radius: 50%;
    background: var(--light-blue);
  }
  .brand__name {
    font-weight: 700;
    font-size: 21px;
    color: var(--white);
  }
  .order-bar__text {
    margin: 0 0 0 10px;
    font-weight: 500;
    font-size: 24px;
    white-space: nowrap;
    color: var(--white);
  }
  .order-bar__url {
    font-style: italic;
    font-size: 22px;
  }
</style>
</head>
<body>
<main class="flyer">

  <header class="header">
    <div class="hotel-mark">
      <span class="hotel-mark__square"></span>
      <span class="hotel-mark__name">Hotel Ardmore</span>
    </div>
    <h1 class="header__title">Next Day<br>Laundry Services</h1>
  </header>

  <div class="laundry-photo" role="img" aria-label="Laundry basket piled with bright orange and red clothes"></div>

  <div class="services-band"></div>
  <h2 class="services-title">Services We Offer</h2>

  <ul class="services-list">
    <li class="services-list__item"><svg class="tick" viewBox="0 0 26 26"><path d="M3 14 L10 21 L23 5" fill="none" stroke="#1f2a6e" stroke-width="4" stroke-linecap="round" stroke-linejoin="round"/></svg>Free pick up and delivery</li>
    <li class="services-list__item"><svg class="tick" viewBox="0 0 26 26"><path d="M3 14 L10 21 L23 5" fill="none" stroke="#1f2a6e" stroke-width="4" stroke-linecap="round" stroke-linejoin="round"/></svg>Email notifications</li>
    <li class="services-list__item"><svg class="tick" viewBox="0 0 26 26"><path d="M3 14 L10 21 L23 5" fill="none" stroke="#1f2a6e" stroke-width="4" stroke-linecap="round" stroke-linejoin="round"/></svg>We use Brisa and Velvo</li>
    <li class="services-list__item"><svg class="tick" viewBox="0 0 26 26"><path d="M3 14 L10 21 L23 5" fill="none" stroke="#1f2a6e" stroke-width="4" stroke-linecap="round" stroke-linejoin="round"/></svg>Smells great</li>
    <li class="services-list__item"><svg class="tick" viewBox="0 0 26 26"><path d="M3 14 L10 21 L23 5" fill="none" stroke="#1f2a6e" stroke-width="4" stroke-linecap="round" stroke-linejoin="round"/></svg>We keep Colors Brighter!</li>
    <li class="services-list__item"><svg class="tick" viewBox="0 0 26 26"><path d="M3 14 L10 21 L23 5" fill="none" stroke="#1f2a6e" stroke-width="4" stroke-linecap="round" stroke-linejoin="round"/></svg>Next day delivery</li>
  </ul>

  <footer class="order-bar">
    <div class="brand">
      <span class="brand__circle"></span>
      <span class="brand__name">quikwashly</span>
    </div>
    <p class="order-bar__text">Place an order at <span class="order-bar__url">www.quikwashly.example</span></p>
  </footer>

</main>
</body>
</html>
```